Medical Centre Website

We need a new design for a medical centre based in Perth, Western Australia called 'Tarvin Grove Medical Centre'.

The medical centre does general practitioner work including general checkups, ecg, heart checks, woman's health and more servicing children and adults. They also do home visits on occasions where the patient cannot attend the centre.

They would like an information/brochure website where visitors can read up on the practice, send email and view their location.

The client wish the design to be clean, fresh and light. The main colours are a light purple/blue and to a dark navy blue. The client would not want the logo to be altered in any way. This includes changing the words colours or the image.

The final design should represent a loving, family friendly practice where patients can come to receive the best treatments.

We just need the end product to be presented to un in a layed psd format. The fonts must be as per the W3C standards.

**IMPORTANT**
I have received heaps of chatlink invites in the past. To treat everyone fairly, I do not add people to my chatlink list as in the past people expected us to give them the prize. If you have questions, please ask them in pixel forum as it may benefit others who are also designing the site. If I need to, I will send a message to the user.
Updates

Hi Designers,

Most designs we have received have been overly cluttered. Are you able to simplify the designs.

Cheers, Dorian

Hi Designers,

Some of the designs are quite attractive but aremore cluttered than I would like. If you have a look at the following design, the design is very simple and straight to the point. A lot of designs have too much wording and the reader can be put off. We are looking something more like:

velmoxa.com.au

I would prefer to see designs and have opened up the contest for a further 7 days.

Designers,

We have received feedback from the client and Quite frankly he don’t really like any of them.They are too cluttered and Americanised. All drab blue colours.
 
If you have a look at template monster, these designs are better and cleaner. We do not want heaps of writing on the front page.

If you look at the eariler examples such as quorbeyclinic.com.au which I did myself, the client loves that simplicity of the site.

```html
<!DOCTYPE html>
<html lang="en">
<head>
<meta charset="utf-8">
<title>Tarvin Grove Medical Centre</title>
<link rel="stylesheet" href="https://fonts.googleapis.com/css2?family=Lato:wght@400;700;900&family=Oswald:wght@400&display=swap">
<style>
  :root {
    --sky: #1aa3e8;
    --orchid: #cc5fd0;
    --ink: #555555;
    --body: #6a6a6a;
    --muted: #7a7a7a;
    --rule: #cfcfcf;
    --field: #eeeeee;
    --paper: #ffffff;
  }
  * { box-sizing: border-box; margin: 0; padding: 0; }
  html, body { width: 1200px; height: 864px; overflow: hidden; background: var(--paper); }
  body { position: relative; font-family: "Lato", Arial, sans-serif; color: var(--body); }
  .abs { position: absolute; }

  /* Hero */
  .hero-photo {
    left: 99px; top: 32px; width: 313px; height: 209px;
    border-radius: 0 0 50% 50% / 0 0 62% 62%;
    background: linear-gradient(180deg, #f4f6f8 0%, #dfe6ec 55%, #c9d3dc 100%);
    box-shadow: 0 8px 10px -4px rgba(0,0,0,0.35);
  }
  .btn-appointment {
    left: 118px; top: 260px; width: 266px; height: 38px;
    background: var(--orchid); color: #fff;
    font: 700 17px/38px "Lato", Arial, sans-serif; text-align: center;
    text-transform: uppercase; letter-spacing: 0.2px;
  }
  .welcome { left: 455px; top: 34px; font: 700 25px/1 "Lato", Arial, sans-serif; color: var(--ink); }
  .site-title {
    left: 455px; top: 66px; font: 900 37px/1 "Lato", Arial, sans-serif;
    color: var(--sky); text-transform: uppercase; letter-spacing: 1.6px;
  }
  .intro { left: 455px; top: 106px; width: 660px; font-size: 13.6px; line-height: 18.6px; }
  .intro p + p { margin-top: 18.6px; }
  .intro-rule { left: 455px; top: 297px; width: 660px; height: 2px; background: var(--orchid); }
  .btn-more {
    left: 1027px; top: 274px; width: 88px; height: 25px; background: var(--orchid); color: #fff;
    font: 700 12px/25px "Lato", Arial, sans-serif; text-align: center; text-transform: uppercase;
  }

  /* Feature blocks */
  .block-title { top: 356px; font: 400 21px/1 "Oswald", "Arial Narrow", sans-serif; color: var(--sky); text-transform: uppercase; }
  .block-box { top: 393px; width: 326px; height: 146px; border: 1px solid var(--rule); }
  .block-media { position: absolute; left: 6px; top: 6px; right: 6px; bottom: 6px; }
  .media-doctors { background: linear-gradient(135deg, #eef3f6 0%, #cfe3ec 45%, #7fc3d6 100%); }
  .media-map { background: linear-gradient(135deg, #e8e4d6 0%, #dcd8c4 40%, #9cc6e4 70%, #7fb2db 100%); }
  .play-icon { position: absolute; left: 140px; top: 47px; }
  .newsletter-copy { position: absolute; left: 13px; top: 14px; width: 300px; font-size: 13.8px; line-height: 19px; color: var(--body); }
  .email-field {
    position: absolute; left: 16px; top: 66px; width: 291px; height: 35px;
    background: var(--field); border: 1px solid #8f8f8f;
    font: 400 13.8px/33px "Lato", Arial, sans-serif; color: #555; padding-left: 8px;
  }
  .btn-submit {
    position: absolute; left: 16px; top: 109px; width: 87px; height: 26px; background: var(--orchid);
    color: #fff; font: 700 12px/26px "Lato", Arial, sans-serif; text-align: center; text-transform: uppercase;
  }

  .soft-rule {
    left: 140px; width: 938px; height: 2px;
    background: linear-gradient(90deg, rgba(60,80,110,0) 0%, rgba(60,80,110,0.7) 50%, rgba(60,80,110,0) 100%);
  }

  /* Footer */
  .foot-col { top: 601px; }
  .foot-title { font: 400 21px/1 "Oswald", "Arial Narrow", sans-serif; color: var(--muted); text-transform: uppercase; margin-bottom: 13px; }
  .foot-list { list-style: none; font-size: 13.8px; line-height: 24.6px; color: var(--muted); }
  .foot-address { font-size: 13.8px; line-height: 18.6px; color: var(--muted); font-style: normal; }
  .foot-address .accent { color: var(--orchid); }
  .social { top: 747px; left: 799px; display: flex; gap: 10px; }
  .social span {
    width: 32px; height: 32px; border-radius: 50%;
    background: radial-gradient(circle at 40% 35%, #ffffff 0%, #e7e9ec 70%, #d3d6da 100%);
    box-shadow: 0 1px 2px rgba(0,0,0,0.25);
  }
  .copyright { left: 0; top: 828px; width: 1200px; text-align: center; font-size: 13.5px; color: #444; }
</style>
</head>
<body>
  <div class="abs hero-photo" role="img" aria-label="Photo of a smiling senior doctor with two colleagues"></div>
  <div class="abs btn-appointment">Get an Appointment</div>

  <h2 class="abs welcome">Welcome To</h2>
  <h1 class="abs site-title">Tarvin Grove Medical Centre</h1>
  <div class="abs intro">
    <p>Phasellus euismod consectetur cursus. Duis eleifend nunc sit amet ipsum laoreet viverra. Cras lectus massa, tristique quis fringilla eu, aliquam ut dui. Pellentesque blandit non nibh eu semper. Maecenas eu dignissim nunc. Praesent hendrerit condimentum ante, a iaculis quam aliquet sed.</p>
    <p>Sed a nunc tempus, blandit mi eleifend, tempor nulla. Nam tincidunt leo in diam tristique, a rhoncus lorem tincidunt. Proin ullamcorper sem quis lacus congue pretium. Nam sit amet lacus eget dolor convallis laoreet. Mauris varius facilisis quam, vitae consequat dolor ultricies eu. Vestibulum non ornare diam. Nullam rhoncus viverra vestibulum.</p>
  </div>
  <div class="abs intro-rule"></div>
  <div class="abs btn-more">Read More</div>

  <h3 class="abs block-title" style="left:90px">Meet a Doctor</h3>
  <h3 class="abs block-title" style="left:441px">Newsletter</h3>
  <h3 class="abs block-title" style="left:790px">Our Location</h3>

  <div class="abs block-box" style="left:90px">
    <div class="block-media media-doctors" role="img" aria-label="Video still of a team of smiling doctors and nurses">
      <svg class="play-icon" width="30" height="30" viewBox="0 0 30 30" aria-hidden="true">
        <circle cx="15" cy="15" r="13.5" fill="#3fb0e6" stroke="#ffffff" stroke-width="2"/>
        <path d="M11.5 9 L21 15 L11.5 21 Z" fill="#ffffff"/>
      </svg>
    </div>
  </div>

  <div class="abs block-box" style="left:441px">
    <p class="newsletter-copy">Get our monthly case history and new check ups schedule subscribe newsletter</p>
    <div class="email-field">Type your email id here..</div>
    <div class="btn-submit">Submit</div>
  </div>

  <div class="abs block-box" style="left:790px">
    <div class="block-media media-map" role="img" aria-label="Street map of Perth showing the centre's location"></div>
  </div>

  <div class="abs soft-rule" style="top:561px"></div>

  <div class="abs foot-col" style="left:99px">
    <h4 class="foot-title">Your Visit</h4>
    <ul class="foot-list">
      <li>Appointments</li><li>Billing &amp; Insurance</li><li>Find A Doctor</li>
      <li>Maps &amp; Directions</li><li>Case History</li><li>Success Story</li>
    </ul>
  </div>
  <div class="abs foot-col" style="left:275px">
    <h4 class="foot-title">Our Services</h4>
    <ul class="foot-list">
      <li>ECG</li><li>Heart Check Ups</li><li>Girls Check Ups</li>
      <li>Boys Checkups</li><li>Adult Checkups</li><li>Different Tests</li>
    </ul>
  </div>
  <div class="abs foot-col" style="left:451px">
    <h4 class="foot-title">Your Visit</h4>
    <ul class="foot-list">
      <li>Appointments</li><li>Billing &amp; Insurance</li><li>Find A Doctor</li><li>Maps &amp; Directions</li>
    </ul>
  </div>
  <div class="abs foot-col" style="left:628px">
    <h4 class="foot-title">Your Visit</h4>
    <ul class="foot-list">
      <li>Appointments</li><li>Billing &amp; Insurance</li><li>Find A Doctor</li><li>Maps &amp; Directions</li>
    </ul>
  </div>
  <div class="abs foot-col" style="left:804px">
    <h4 class="foot-title">Tarvin Grove Medical Centre</h4>
    <address class="foot-address">
      18 Fernhollow Rd, Suite 4,<br>
      WA 6012, Perth,<br>
      Australia<br>
      Phone No: <span class="accent">(+08) 5550 2871</span><br>
      Email id: <span class="accent">info@tgmc-care.com</span>
    </address>
  </div>
  <div class="abs social" aria-label="Social links">
    <span></span><span></span><span></span>
  </div>

  <div class="abs soft-rule" style="top:817px"></div>
  <p class="abs copyright">© 2013, All Rights Reserved, Tarvin Grove Medical Centre</p>
</body>
</html>
```